Business is called "Kestrel Ledger". Accounting and tax services.

I need a flyer for my new business "Kestrel Ledger". I am an individual accountant working for himself on the Sunshine Coast in Queensland Australia. I would like to see designs that communicate reliability and trust. I believe my point of difference is that I am always available to my clients and I will cap my number of clients to ensure I can service them properly. Accountants in general seem to have a bad reputation for not responding to clients in a timely fashion, whether by email or phone. This is where I intend to differentiate myself. I have included my business card for ideas on colour and for contact information. I have also included some logo's that should go on the flyer. With the QLA logo, the words "Kestrel Ledger is a QLA Business" needs to be written either above, below or to the right hand side (as per the business card).

Target Market(s)

Small business owners and individuals requiring taxation and financials

Industry/Entity Type

Public Accounting

Font styles to use
Serif

Requirements
Must have
• Supplied logo's, accounting style pictures etc
Services: Small Business Taxation
Company & Trust Tax Returns
Rental Property Returns
Capital Gains Tax
Individual Tax Returns
BAS and IAS lodgements
Nice to have
• Needs to convey a sense of being reliable and responds to clients quickly.
Should not have
• My name

```html
<!DOCTYPE html>
<html lang="en">
<head>
<meta charset="utf-8">
<title>Kestrel Ledger Flyer</title>
<link rel="stylesheet" href="https://fonts.googleapis.com/css2?family=Lora:wght@400;500;600;700&display=swap">
<style>
  :root {
    --green: #23a383;
    --charcoal: #2b2c2e;
    --text: #2f3033;
    --muted: #4a4b4e;
    --panel: #eeeeec;
    --white: #ffffff;
    --navy: #0f4f9a;
    --sky: #1bb3e8;
    --lime: #c7d92b;
  }
  * { box-sizing: border-box; margin: 0; padding: 0; }
  html, body { width: 900px; height: 1200px; overflow: hidden; background: var(--white); }
  body { font-family: "Lora", serif; color: var(--text); }
  .flyer { position: relative; width: 900px; height: 1200px; overflow: hidden; background: var(--white); }

  .hero-photo {
    position: absolute; left: 0; top: 0; width: 900px; height: 580px;
    background: linear-gradient(115deg, #f7f8f9 0%, #eef1f3 38%, #c9d3dc 58%, #2b3a55 78%, #1c2740 100%);
  }
  .brand { position: absolute; left: 54px; top: 40px; width: 300px; text-align: center; }
  .brand-mark { display: block; margin: 0 auto; width: 112px; height: 112px; border: 3px solid var(--charcoal); border-radius: 50%; }
  .brand-name { margin-top: 24px; font-size: 24px; font-weight: 500; letter-spacing: 8px; color: var(--charcoal); white-space: nowrap; }

  .headline-band {
    position: absolute; left: 54px; top: 517px; width: 598px; height: 123px;
    background: var(--green); padding: 10px 0 0 22px;
  }
  .headline-band p { color: var(--white); font-size: 31px; line-height: 35px; font-weight: 700; letter-spacing: .3px; white-space: nowrap; }
  .headline-band .light { font-weight: 400; }

  .difference { position: absolute; left: 73px; top: 674px; width: 400px; }
  .difference h2 { font-size: 22px; line-height: 30px; font-weight: 700; color: var(--charcoal); }
  .difference ul { list-style: none; margin-top: 8px; position: relative; }
  .difference ul::before { content: ""; position: absolute; left: 7px; top: 12px; bottom: 12px; width: 2px; background: var(--green); }
  .difference li { position: relative; padding-left: 30px; font-size: 17.5px; height: 31px; line-height: 24px; }
  .difference li::before { content: ""; position: absolute; left: 0; top: 5px; width: 11px; height: 11px; border-radius: 50%; background: var(--charcoal); border: 2.5px solid var(--green); }

  .about { position: absolute; left: 75px; top: 826px; width: 365px; }
  .about h3 { font-size: 14.5px; font-weight: 700; color: var(--green); }
  .about p { margin-top: 2px; font-size: 13.5px; line-height: 19px; color: var(--muted); }
  .about strong { font-weight: 700; color: var(--charcoal); }

  .call { position: absolute; left: 75px; top: 1008px; width: 318px; height: 60px; border: 1px solid #9a9a9a; border-top: none; }
  .call::before { content: ""; position: absolute; left: 0; top: 0; width: 40px; border-top: 1px solid #9a9a9a; }
  .call::after { content: ""; position: absolute; right: 0; top: 0; width: 40px; border-top: 1px solid #9a9a9a; }
  .call-label { position: absolute; left: 0; right: 0; top: -19px; text-align: center; font-size: 30px; line-height: 38px; font-weight: 500; color: var(--charcoal); }
  .phone-pill {
    position: absolute; left: 10px; top: 26px; width: 298px; height: 41px; border-radius: 21px;
    background: var(--green); box-shadow: 0 0 0 2px var(--white), 0 0 0 3px var(--green);
    display: flex; align-items: center; justify-content: center; gap: 8px;
    color: var(--white); font-size: 28px; font-weight: 700;
  }
  .phone-pill svg { width: 24px; height: 24px; }

  .services { position: absolute; left: 527px; top: 680px; width: 320px; height: 376px;
    background: linear-gradient(90deg, var(--panel) 0%, #f7f7f6 60%, #eaeae8 100%); }
  .services-tag { position: absolute; left: -14px; top: 24px; width: 264px; height: 35px; background: var(--charcoal);
    color: var(--white); font-size: 20px; font-weight: 700; line-height: 35px; padding-left: 22px; letter-spacing: .5px; }
  .services-tag::after { content: ""; position: absolute; left: 0; top: 35px; border-top: 12px solid #555; border-left: 12px solid transparent; }
  .services ul { list-style: none; position: absolute; left: 13px; top: 90px; width: 300px; }
  .services li { display: flex; gap: 14px; font-size: 19.5px; line-height: 26px; margin-bottom: 14px; color: var(--charcoal); white-space: nowrap; }
  .services li svg { flex: 0 0 22px; width: 22px; height: 22px; margin-top: 2px; }

  .contact { position: absolute; left: 72px; top: 1106px; }
  .contact .lead { font-size: 13px; line-height: 18px; color: var(--muted); }
  .contact p { display: flex; align-items: center; gap: 5px; font-size: 18.5px; font-weight: 500; line-height: 22px; }
  .contact .web { color: var(--green); }
  .contact svg { width: 13px; height: 13px; }

  .credentials { position: absolute; left: 428px; top: 1103px; height: 60px; display: flex; align-items: center; }
  .badge { width: 58px; height: 58px; border-radius: 50%; border: 2px solid #666; background: var(--lime); box-shadow: inset 0 0 0 9px var(--white); }
  .agent { margin-left: 8px; font-size: 9px; line-height: 12px; color: var(--charcoal); width: 50px; }
  .rule { width: 1px; height: 46px; background: #999; margin: 0 8px; }
  .partner { display: flex; align-items: center; gap: 6px; font-size: 19px; font-weight: 600; color: var(--navy); }
  .partner-square { width: 18px; height: 18px; background: var(--navy); }
  .member-note { margin-left: 10px; font-size: 9.5px; line-height: 12px; font-weight: 600; color: var(--charcoal); width: 112px; }
  .software { display: flex; align-items: center; gap: 5px; font-size: 13px; font-weight: 600; color: var(--sky); }
  .software-dot { width: 14px; height: 14px; border-radius: 50%; background: var(--sky); }

  .footer-bar { position: absolute; left: 0; bottom: 0; width: 900px; height: 9px; display: flex; }
  .footer-bar span:first-child { flex: 1; background: var(--charcoal); }
  .footer-bar span:last-child { flex: 1; background: var(--green); }
</style>
</head>
<body>
<div class="flyer">
  <div class="hero-photo" role="img" aria-label="Photo of two accountants in suits reviewing a tablet at a bright office desk with a laptop"></div>

  <div class="brand">
    <span class="brand-mark"></span>
    <div class="brand-name">KESTREL LEDGER</div>
  </div>

  <div class="headline-band">
    <p>PROFESSIONAL ACCOUNTING</p>
    <p><span class="light">AND</span> TAXATION SERVICES</p>
    <p>SUNSHINE COAST</p>
  </div>

  <section class="difference">
    <h2>The Kestrel Ledger Difference</h2>
    <ul>
      <li>Personal Service</li>
      <li>Prompt reply to all client queries</li>
      <li>Highly qualified Accountant</li>
    </ul>
  </section>

  <section class="about">
    <h3>About Me</h3>
    <p>I have lived on the Sunshine Coast for the past 18 years and know its local businesses well. I am a <strong>Certified Practising Accountant</strong>, I have a Bachelor of Commerce majoring in Accounting &amp; Finance and a Master of Taxation from Eastbrook University.</p>
  </section>

  <div class="call">
    <div class="call-label">CALL TODAY</div>
    <div class="phone-pill">
      <svg viewBox="0 0 24 24" fill="none" stroke="#fff" stroke-width="2.2" stroke-linecap="round"><path d="M6 3l3 4-2 2c1 3 4 6 7 7l2-2 4 3-2 3C10 20 4 14 3 5z"/><path d="M14 3a7 7 0 0 1 7 7"/><path d="M14 7a3 3 0 0 1 3 3"/></svg>
      0412 555 019
    </div>
  </div>

  <section class="services">
    <div class="services-tag">SPECIALISING IN</div>
    <ul>
      <li><svg viewBox="0 0 24 24" fill="none" stroke="#23a383" stroke-width="2"><path d="M20 9a9 9 0 1 1-4-5"/><path d="M7 11l4 4 10-11"/></svg><span>Small Business Taxation</span></li>
      <li><svg viewBox="0 0 24 24" fill="none" stroke="#23a383" stroke-width="2"><path d="M20 9a9 9 0 1 1-4-5"/><path d="M7 11l4 4 10-11"/></svg><span>Company &amp; Trust Tax<br>Returns</span></li>
      <li><svg viewBox="0 0 24 24" fill="none" stroke="#23a383" stroke-width="2"><path d="M20 9a9 9 0 1 1-4-5"/><path d="M7 11l4 4 10-11"/></svg><span>Rental Property Returns</span></li>
      <li><svg viewBox="0 0 24 24" fill="none" stroke="#23a383" stroke-width="2"><path d="M20 9a9 9 0 1 1-4-5"/><path d="M7 11l4 4 10-11"/></svg><span>Capital Gains Tax</span></li>
      <li><svg viewBox="0 0 24 24" fill="none" stroke="#23a383" stroke-width="2"><path d="M20 9a9 9 0 1 1-4-5"/><path d="M7 11l4 4 10-11"/></svg><span>Individual Tax Returns</span></li>
      <li><svg viewBox="0 0 24 24" fill="none" stroke="#23a383" stroke-width="2"><path d="M20 9a9 9 0 1 1-4-5"/><path d="M7 11l4 4 10-11"/></svg><span>BAS and IAS lodgements</span></li>
    </ul>
  </section>

  <div class="contact">
    <div class="lead">For more info, please visit</div>
    <p class="web"><svg viewBox="0 0 16 16" fill="none" stroke="#23a383" stroke-width="1.3"><circle cx="8" cy="8" r="7"/><path d="M1 8h14M8 1c3 3 3 11 0 14M8 1c-3 3-3 11 0 14"/></svg>www.kestrelledger.com.au</p>
    <p><svg viewBox="0 0 16 16"><circle cx="8" cy="8" r="8" fill="#23a383"/><rect x="4" y="5.5" width="8" height="5.5" fill="none" stroke="#fff" stroke-width="1"/><path d="M4 5.5l4 3 4-3" fill="none" stroke="#fff" stroke-width="1"/></svg>hello@kestrelledger.com.au</p>
  </div>

  <div class="credentials">
    <div class="badge"></div>
    <div class="agent">Tax agent 10293847</div>
    <div class="rule"></div>
    <div class="partner"><span class="partner-square"></span>QLA</div>
    <div class="member-note">Kestrel Ledger is a QLA Business</div>
    <div class="rule"></div>
    <div class="software"><span class="software-dot"></span>Ledgerly</div>
  </div>

  <div class="footer-bar"><span></span><span></span></div>
</div>
</body>
</html>
```